Cloud Software Services Business Needs New Website Design

Our client is looking for a really modern design for their cloud services company. We have a logo, but apart from that, if you read the brief fully and digest the wireframes, we hope you will come up with a really amazing end product.

The design of the website should be professional and trustworthy, it is there to inspire confidence in the services and softwares, as well as emphasising the track record of TWN and relative knowledge and competencies.

Given all the cloud-related communications in the messaging on the site, we will need this in either the imagery or icons in the site so that we can connect the messaging with the service offering.

The brand, being black, gives full range for the designer to present a palette that serves the brand, not forgetting the audience are generally IT decision-makers.

Target Market(s)

Managers and Directors Responsible for IT/Cloud Infrastructure

Industry/Entity Type

IT Technology

Number of Pages Required

5+ page

Font styles to use
Sans Serif

Requirements
Must have
• Initial designs which match the brief and wireframes, focus on the homepage and the winning designer will need to supply the internal pages for the website.
Nice to have
• Clearly considered professional website designs, with consistent design work and branding. If choosing stock imagery, then from PixVault Basics please.
Should not have
• Not too much colour, or too consumer/youthful.

```html
<!DOCTYPE html>
<html lang="en">
<head>
<meta charset="utf-8">
<title>TWN – Cloud Based Services &amp; Solutions</title>
<link href="https://fonts.googleapis.com/css2?family=Poppins:wght@300;400;500;600;700&display=swap" rel="stylesheet">
<style>
:root{
  --black:#000;
  --white:#fff;
  --yellow:#ffe100;
  --grey-bg:#f5f5f5;
  --card-bg:#f6f6f6;
  --text:#111;
  --muted:#666;
  --field:#d4d4d4;
}
*{box-sizing:border-box;margin:0;padding:0}
html,body{width:1200px;height:3559px;overflow:hidden}
body{font-family:'Poppins',sans-serif;color:var(--text);background:var(--white);position:relative}
.abs{position:absolute}
section,header,footer{position:absolute;left:0;width:1200px}

/* hero */
.hero{top:0;height:637px;background:var(--black);color:var(--white)}
.brand{left:61px;top:12px;font-size:54px;font-weight:600;letter-spacing:2px;color:var(--white);line-height:76px}
.nav{top:33px;left:0;font-size:13px}
.nav a{position:absolute;color:var(--white);text-decoration:none;white-space:nowrap}
.btn{display:flex;align-items:center;justify-content:center;background:var(--yellow);color:var(--black);border-radius:20px;font-size:13px}
.signup{left:1056px;top:25px;width:83px;height:37px}
.hero-title{left:62px;top:196px;font-size:52px;line-height:57px;font-weight:400;letter-spacing:.5px}
.hero-text{left:61px;top:326px;width:540px;font-size:12.5px;line-height:21px;font-weight:300}
.quote{left:61px;top:411px;width:114px;height:36px}
.badge{width:96px;height:96px;border-radius:50%;background:var(--white);border:2px solid var(--yellow);display:flex;align-items:center;justify-content:center;font-size:15px;font-weight:600;color:#222}
.core{left:763px;top:217px;width:220px;height:220px;border-radius:50%;background:var(--white);display:flex;align-items:center;justify-content:center;font-size:60px;font-weight:600;color:var(--black)}

/* partner strip */
.partners{top:637px;height:143px;background:var(--grey-bg)}
.partner{top:48px;height:46px;display:flex;align-items:center;gap:8px;font-size:24px;font-weight:500;color:#333;white-space:nowrap}
.partner i{display:block;width:22px;height:22px;border-radius:50%;background:#333}

/* services */
.services{top:780px;height:730px}
.svc{width:182px;border-radius:6px;background:var(--card-bg);display:flex;flex-direction:column;align-items:center;justify-content:center;text-align:center;font-size:17px;font-weight:500;line-height:26px;gap:10px}
.svc svg{width:54px;height:54px;fill:none;stroke:currentColor;stroke-width:2}
.svc.dark{background:var(--black);color:var(--white)}
.sec-title{font-size:31px;font-weight:400}
.sec-title b{font-weight:700}
.svc-head{left:747px;top:203px}
.svc-text{left:747px;top:254px;width:395px;font-size:12.5px;line-height:21px;color:var(--muted);font-weight:300}
.svc-text p+p{margin-top:9px}
.read{left:746px;top:445px;width:108px;height:36px;color:var(--white);font-size:12.5px}

/* software */
.software{top:1510px;height:584px;background:var(--black);color:var(--white)}
.center{left:0;width:1200px;text-align:center}
.sub{font-size:12.5px;line-height:21px;font-weight:300}
.sub span{display:block;width:520px;margin:0 auto}
.team-photo{left:61px;top:165px;width:500px;height:341px;border-radius:120px 30px 120px 30px;background:linear-gradient(135deg,#0c2a3a 0%,#2f6f86 45%,#0a1c26 100%)}
.timeline{left:624px;top:154px;width:1px;height:308px;background:#777}
.dot{width:11px;height:11px;border-radius:50%;background:var(--yellow)}
.step{left:649px;font-size:17px;line-height:26px}
.info-card{left:880px;top:187px;width:292px;height:337px;border-radius:8px;background:#f7fafd;color:#555;padding:44px 26px 0 33px;font-size:12.5px;line-height:22.6px;font-weight:300}
.pointer{left:865px;top:255px;width:0;height:0;border-top:12px solid transparent;border-bottom:12px solid transparent;border-right:15px solid var(--yellow)}

/* blog */
.blog{top:2094px;height:620px}
.post{top:190px;width:340px}
.post-img{width:340px;height:232px;border-radius:8px;position:relative}
.date{position:absolute;left:0;top:0;width:55px;height:54px;background:var(--yellow);border-radius:6px 0 6px 0;color:var(--white);font-size:12.5px;line-height:15px;padding:10px 0 0 22px}
.post h3{margin-top:20px;font-size:17px;font-weight:500;padding-left:2px}
.post p{margin-top:8px;font-size:12.5px;line-height:22px;color:var(--muted);font-weight:300;width:330px;padding-left:2px}
.post a{display:block;margin-top:10px;color:var(--yellow);font-size:16px;text-decoration:none;padding-left:2px}

/* contact */
.contact{top:2714px;height:520px}
.phone-big{font-size:16px;font-weight:600;color:var(--yellow)}
.field{width:338px;height:34px;border:1px solid var(--field);border-radius:2px;font-size:12.5px;color:#555;padding:8px 14px;font-weight:300}
.submit{left:558px;top:430px;width:84px;height:35px;color:var(--white);font-size:12.5px}

/* footer */
.footer{top:3234px;height:325px;background:var(--black);color:var(--white)}
.foot-brand{left:58px;top:42px;font-size:104px;font-weight:600;letter-spacing:3px;line-height:130px}
.social{top:215px;width:30px;height:30px;border-radius:50%;background:var(--white)}
.col h4{font-size:17px;font-weight:500;padding-bottom:6px;border-bottom:1px solid var(--white);display:inline-block}
.col ul{list-style:none;margin-top:16px;font-size:12.5px;line-height:28px}
.col .mark{width:4px;height:3px;background:var(--yellow);margin-top:-2px;margin-left:70px}
.contact-row{display:flex;align-items:center;gap:12px;font-size:12.5px;height:26px;margin-bottom:13px}
.contact-row svg{width:20px;height:20px;fill:none;stroke:var(--yellow);stroke-width:1.6}
.divider{left:0;top:285px;width:1200px;height:1px;background:#333}
.copy{top:296px;font-size:12.5px}
</style>
</head>
<body>

<header class="hero">
  <div class="abs brand">TWN</div>
  <nav class="abs nav">
    <a style="left:569px">Home</a>
    <a style="left:640px">Cloud</a>
    <a style="left:711px">Services</a>
    <a style="left:801px">Software</a>
    <a style="left:891px">Blog</a>
    <a style="left:954px">Contact Us</a>
  </nav>
  <a class="abs btn signup">Sign Up</a>

  <h1 class="abs hero-title">Cloud Based<br>Services &amp; Solutions</h1>
  <p class="abs hero-text">It has survived not only five centuries, but also the leap into electronic typesetting, remaining essentially unchanged.</p>
  <a class="abs btn quote">Get A Quote</a>

  <svg class="abs" style="left:653px;top:107px" width="440" height="440" viewBox="0 0 440 440">
    <circle cx="220" cy="220" r="210" fill="none" stroke="#fff" stroke-width="1"/>
    <circle cx="220" cy="220" r="155" fill="none" stroke="#fff" stroke-width="1"/>
  </svg>
  <div class="abs core">TWN</div>
  <div class="abs badge" style="left:677px;top:118px">Stratus</div>
  <div class="abs badge" style="left:960px;top:100px">Nimbo</div>
  <div class="abs badge" style="left:1040px;top:317px">Kumo</div>
  <div class="abs badge" style="left:638px;top:388px;font-size:13px">Driftwave</div>
  <div class="abs badge" style="left:874px;top:495px">Orbita</div>
</header>

<section class="partners">
  <div class="abs partner" style="left:59px"><i></i>Tradewind</div>
  <div class="abs partner" style="left:250px">Loopa</div>
  <div class="abs partner" style="left:394px">Corvo</div>
  <div class="abs partner" style="left:515px"><i></i>Vantra</div>
  <div class="abs partner" style="left:720px"><i></i>Brightmind</div>
</section>

<section class="services">
  <div class="abs svc" style="left:257px;top:86px;height:174px">
    <svg viewBox="0 0 54 54"><path d="M14 40h26a8 8 0 0 0 0-16 12 12 0 0 0-23-3 9 9 0 0 0-3 19z"/><circle cx="43" cy="12" r="6"/><path d="M40 12l2 2 4-4"/></svg>
    Cloud<br>Enablement</div>
  <div class="abs svc" style="left:458px;top:123px;height:198px">
    <svg viewBox="0 0 54 54"><rect x="4" y="6" width="46" height="42" rx="2"/><path d="M4 14h46"/><circle cx="27" cy="31" r="6"/><circle cx="27" cy="31" r="11" stroke-dasharray="4 3"/></svg>
    Site Reliability<br>Engineering</div>
  <div class="abs svc" style="left:59px;top:225px;height:176px">
    <svg viewBox="0 0 54 54"><circle cx="24" cy="40" r="10"/><path d="M24 35v10M21 38h5M21 42h5"/><path d="M14 24h22a7 7 0 0 0 0-14 10 10 0 0 0-19-2 8 8 0 0 0-3 16z"/><circle cx="40" cy="26" r="6"/></svg>
    Cloud Cost<br>Review</div>
  <div class="abs svc dark" style="left:257px;top:278px;height:174px">
    <svg viewBox="0 0 54 54"><circle cx="32" cy="18" r="7"/><circle cx="32" cy="18" r="13" stroke-dasharray="4 3"/><circle cx="18" cy="34" r="6"/><circle cx="18" cy="34" r="11" stroke-dasharray="4 3"/></svg>
    Cloud Dev Ops</div>
  <div class="abs svc" style="left:458px;top:340px;height:174px">
    <svg viewBox="0 0 54 54"><rect x="16" y="14" width="22" height="28" rx="2"/><rect x="22" y="26" width="10" height="8"/><path d="M24 26v-3a3 3 0 0 1 6 0v3"/><rect x="4" y="4" width="8" height="8"/><rect x="42" y="4" width="8" height="8"/><rect x="4" y="42" width="8" height="8"/><rect x="42" y="42" width="8" height="8"/></svg>
    Security &amp;<br>Compliance</div>
  <div class="abs svc" style="left:59px;top:419px;height:198px">
    <svg viewBox="0 0 54 54"><path d="M14 20h24a7 7 0 0 0 0-14 10 10 0 0 0-19-1 8 8 0 0 0-5 15z"/><rect x="6" y="24" width="30" height="20" rx="2"/><path d="M16 50h10M21 44v6"/><circle cx="42" cy="32" r="6"/></svg>
    Migration<br>Planning &amp;<br>Execution</div>
  <div class="abs svc" style="left:257px;top:473px;height:173px">
    <svg viewBox="0 0 54 54"><path d="M12 36h30a8 8 0 0 0 0-16 13 13 0 0 0-25-3 10 10 0 0 0-5 19z"/><circle cx="27" cy="30" r="6"/><circle cx="27" cy="30" r="11" stroke-dasharray="4 3"/></svg>
    Cloud<br>Optimisation</div>

  <h2 class="abs sec-title svc-head"><b>Our</b> Services</h2>
  <div class="abs svc-text">
    <p>Lorem Ipsum is simply dummy text of the printing and typesetting industry. Lorem Ipsum has been the industry's standard dummy text ever since the 1500s, when an unknown printer took a galley of type and scrambled it to make a type specimen book.</p>
    <p>It has survived not only five centuries, but also the leap into electronic typesetting, remaining essentially unchanged.</p>
  </div>
  <a class="abs btn read">Read More</a>
</section>

<section class="software">
  <h2 class="abs center sec-title" style="top:44px">Software</h2>
  <p class="abs center sub" style="top:91px"><span>Lorem Ipsum is simply dummy text of the printing and typesetting industry. Lorem Ipsum has been the industry's standard dummy text.</span></p>
  <div class="abs team-photo" role="img" aria-label="Two engineers working on a laptop in a server room"></div>
  <div class="abs timeline"></div>
  <div class="abs dot" style="left:619px;top:225px"></div>
  <div class="abs dot" style="left:619px;top:345px"></div>
  <p class="abs step" style="top:217px">Skyport</p>
  <p class="abs step" style="top:330px">CodeShift [inc Vexa Test<br>references]</p>
  <div class="abs pointer"></div>
  <div class="abs info-card">Lorem Ipsum is simply dummy text of the printing and typesetting industry. Lorem Ipsum has been the industry's standard dummy text ever since the 1500s, when an unknown printer took a galley of type and scrambled it to make a type specimen book. It has survived not only five centuries, but also the leap into electronic typesetting, remaining essentially unchanged.</div>
</section>

<section class="blog">
  <h2 class="abs center sec-title" style="top:82px"><b>Our</b> Latest Blog</h2>
  <p class="abs center sub" style="top:130px;color:var(--muted)"><span>Lorem Ipsum is simply dummy text of the printing and typesetting industry. Lorem Ipsum has been the industry's standard dummy text.</span></p>

  <article class="abs post" style="left:59px">
    <div class="post-img" role="img" aria-label="Engineer with a laptop between server racks" style="background:linear-gradient(135deg,#0b2533,#1f5b6e 55%,#071821)"><div class="date">15<br>jun</div></div>
    <h3>Lorem Ipsum is simply dummy text.</h3>
    <p>Lorem Ipsum is simply dummy text of the printing and typesetting industry.</p>
    <a>Read more</a>
  </article>
  <article class="abs post" style="left:427px">
    <div class="post-img" role="img" aria-label="Hand holding a tablet with a glowing cloud above it" style="background:radial-gradient(circle at 50% 45%,#3b6f86,#0d1a22 60%,#05090c)"><div class="date">15<br>Aug</div></div>
    <h3>Lorem Ipsum is simply dummy text.</h3>
    <p>Lorem Ipsum is simply dummy text of the printing and typesetting industry.</p>
    <a>Read more</a>
  </article>
  <article class="abs post" style="left:800px">
    <div class="post-img" role="img" aria-label="Two developers smiling at a laptop in an office" style="background:linear-gradient(135deg,#1c2f3f,#4a6477 50%,#15222e)"><div class="date">15<br>sep</div></div>
    <h3>Lorem Ipsum is simply dummy text.</h3>
    <p>Lorem Ipsum is simply dummy text of the printing and typesetting industry.</p>
    <a>Read more</a>
  </article>
</section>

<section class="contact">
  <h2 class="abs center sec-title" style="top:60px"><b>Contact</b> Us</h2>
  <p class="abs center sub" style="top:111px;color:#555">Have An any questions for Contact Us Today!</p>
  <p class="abs center phone-big" style="top:142px">123 456 7890</p>
  <div class="abs field" style="left:250px;top:186px">Name*</div>
  <div class="abs field" style="left:250px;top:237px">E-mail*</div>
  <div class="abs field" style="left:250px;top:293px">Phone No.*</div>
  <div class="abs field" style="left:250px;top:341px">Subject*</div>
  <div class="abs field" style="left:612px;top:186px;height:189px">Massage*</div>
  <a class="abs btn submit">Submit</a>
</section>

<footer class="footer">
  <div class="abs foot-brand">TWN</div>
  <span class="abs social" style="left:60px" aria-label="Social profile 1"></span>
  <span class="abs social" style="left:101px;background:var(--yellow)" aria-label="Social profile 2"></span>
  <span class="abs social" style="left:141px" aria-label="Social profile 3"></span>

  <div class="abs col" style="left:337px;top:53px">
    <h4>Quick Links</h4><div class="mark"></div>
    <ul><li>Home</li><li>Cloud</li><li>Services</li><li>Software</li><li>Blog</li><li>Contact Us</li></ul>
  </div>
  <div class="abs col" style="left:613px;top:53px">
    <h4>Company</h4><div class="mark"></div>
    <ul><li>terms of use</li><li>Privacy and Cookies Policy</li></ul>
  </div>
  <div class="abs col" style="left:889px;top:53px">
    <h4>Contact Us</h4><div class="mark"></div>
    <div style="margin-top:16px">
      <div class="contact-row"><svg viewBox="0 0 20 20"><path d="M10 18s6-6 6-10a6 6 0 0 0-12 0c0 4 6 10 6 10z"/><circle cx="10" cy="8" r="2"/></svg>123 Lorem Ipsum Is a dummy text.</div>
      <div class="contact-row" style="font-weight:600"><svg viewBox="0 0 20 20"><path d="M4 3h4l2 4-2 2a10 10 0 0 0 4 4l2-2 4 2v4a2 2 0 0 1-2 1A15 15 0 0 1 3 5a2 2 0 0 1 1-2z"/></svg>123 456 7890</div>
      <div class="contact-row"><svg viewBox="0 0 20 20"><rect x="2" y="4" width="16" height="12"/><path d="M2 4l8 7 8-7"/></svg>info@TWN.com</div>
    </div>
  </div>
  <div class="abs divider"></div>
  <p class="abs center copy">Copyright ©&nbsp; 2022 Nimbusverse.All rights reserved.</p>
</footer>

</body>
</html>
```